TBNW site redesign

Please redesign a home page with content provided. PSD only - no coding
Can use any images from Vexelmarq.com

Please create a site design that more clearly illustrates the client's services and expertise. We are looking for a high-end design.

Any images used must be generic or of Dallas TX.

Fonts: Any
Colors: Match to logo
Look: Modern - Professional

Target Market(s)

medium-large business owners

Number of Pages Required

1 page

Font styles to use
Serif
Sans Serif

Requirements
Must have
• cohesive professional design
• high end look
• Match to logo

```html
<!DOCTYPE html>
<html lang="en">
<head>
<meta charset="utf-8">
<title>TBNW | Tenant Representation</title>
<link href="https://fonts.googleapis.com/css2?family=Montserrat:wght@400;600;700&family=Open+Sans:wght@400;600&display=swap" rel="stylesheet">
<style>
:root{
  --red:#c8161d;
  --red-dark:#a51017;
  --ink:#2c2c2c;
  --muted:#8a8a8a;
  --light:#f4f4f4;
  --dark:#333538;
  --darker:#2a2b2e;
  --white:#ffffff;
}
*{box-sizing:border-box;margin:0;padding:0}
html,body{width:1200px;height:2612px;overflow:hidden}
body{font-family:"Open Sans",Arial,sans-serif;color:var(--ink);background:var(--white);position:relative}
h1,h2,h3,.btn,.nav a{font-family:"Montserrat",Arial,sans-serif}

/* hero */
.hero{position:absolute;left:0;top:0;width:1200px;height:560px;overflow:hidden}
.hero-photo{position:absolute;inset:0;background:linear-gradient(100deg,#1d2a3a 0%,#3e5a78 40%,#7d97b0 62%,#c4ccd4 80%,#8c939b 100%)}
.hero-shade{position:absolute;inset:0;background:linear-gradient(90deg,rgba(20,25,35,.55),rgba(20,25,35,.1) 60%,rgba(0,0,0,0))}
.topbar{position:absolute;left:0;top:0;width:1200px;height:76px}
.logo{position:absolute;left:220px;top:0;width:104px;height:70px;background:var(--red);display:flex;align-items:center;justify-content:center}
.logo span{font-family:"Montserrat",sans-serif;font-weight:700;color:var(--white);font-size:26px;letter-spacing:1px}
.nav{position:absolute;right:220px;top:26px;display:flex;gap:22px}
.nav a{color:var(--white);font-size:11px;font-weight:600;text-decoration:none;letter-spacing:.5px}
.hero h1{position:absolute;left:220px;top:196px;width:470px;color:var(--white);font-size:34px;line-height:1.25;font-weight:600}
.hero .lede{position:absolute;left:220px;top:290px;width:360px;color:#e6e9ee;font-size:12px;line-height:1.6}
.btn{display:inline-block;font-size:12px;font-weight:600;color:var(--white);background:var(--red);padding:14px 22px;text-decoration:none}
.hero .cta{position:absolute;left:220px;top:344px}
.hero .phone{position:absolute;left:398px;top:352px;color:var(--white);font-family:"Montserrat",sans-serif;font-size:18px;font-weight:600;display:flex;align-items:center;gap:10px}
.lead-form{position:absolute;left:700px;top:88px;width:282px;height:420px;background:rgba(40,40,44,.88);padding:26px 26px}
.lead-form h3{color:var(--white);font-size:18px;line-height:1.35;font-weight:600;margin-bottom:22px}
.field{height:40px;border-bottom:1px solid rgba(255,255,255,.25);color:#cfd2d6;font-size:11px;padding-top:14px}
.field.tall{height:80px}
.lead-form .btn{display:block;text-align:center;margin-top:30px}

/* why */
.why{position:absolute;left:0;top:560px;width:1200px;height:520px;background:var(--white)}
.section-title{text-align:center;font-size:22px;font-weight:600;color:var(--ink)}
.section-title::after{content:"";display:block;width:50px;height:2px;background:var(--red);margin:14px auto 0}
.why .section-title{position:absolute;left:0;right:0;top:112px}
.features{position:absolute;left:225px;top:220px;width:750px;display:grid;grid-template-columns:1fr 1fr;gap:40px 60px}
.feature{display:flex;gap:18px}
.feature .icon{flex:none;width:44px;height:44px;background:var(--red);display:flex;align-items:center;justify-content:center}
.feature h3{font-size:14px;font-weight:600;margin-bottom:8px}
.feature p{font-size:11px;line-height:1.6;color:var(--muted)}

/* founder */
.founder{position:absolute;left:220px;top:1100px;width:760px;height:220px;background:var(--white);box-shadow:0 4px 24px rgba(0,0,0,.08)}
.founder-photo{position:absolute;left:0;top:0;width:180px;height:220px;background:linear-gradient(180deg,#6f7378,#2d2f33)}
.founder-text{position:absolute;left:210px;top:28px;width:460px;font-size:11px;line-height:1.7;color:var(--muted)}
.founder-name{position:absolute;left:210px;top:176px;font-size:12px;color:var(--ink);font-weight:600}
.founder-name span{font-weight:400;color:var(--muted)}
.founder-next{position:absolute;left:680px;top:90px;width:40px;height:40px;background:var(--red);display:flex;align-items:center;justify-content:center}

/* testimonial */
.testimonials{position:absolute;left:0;top:1400px;width:1200px;height:520px;background:linear-gradient(180deg,#ececec,#dcdcdc)}
.testimonials-photo{position:absolute;inset:0;background:linear-gradient(180deg,rgba(255,255,255,.7),rgba(215,215,215,.6))}
.testimonials .section-title{position:absolute;left:0;right:0;top:60px}
.quote-card{position:absolute;left:390px;top:200px;width:420px;height:150px;background:var(--white);padding:24px 30px;text-align:center;font-size:11px;line-height:1.7;color:var(--muted);box-shadow:0 4px 20px rgba(0,0,0,.08)}
.quote-card .who{display:block;margin-top:10px;color:var(--ink);font-weight:600}
.quote-card::after{content:"";position:absolute;left:200px;bottom:-10px;border:10px solid transparent;border-bottom:0;border-top-color:var(--white)}
.ghost{position:absolute;top:220px;width:240px;font-size:10px;line-height:1.7;color:#b4b4b4}
.avatar{position:absolute;width:34px;height:34px;border-radius:50%;background:linear-gradient(180deg,#9a9a9a,#555)}

/* appointment band */
.band{position:absolute;left:0;top:1920px;width:1200px;height:160px;background:var(--red)}
.band p{position:absolute;left:220px;top:52px;width:440px;color:var(--white);font-size:15px;line-height:1.55;font-weight:600;font-family:"Montserrat",sans-serif}
.band .btn-outline{position:absolute;left:790px;top:58px;width:190px;text-align:center;border:1px solid var(--white);color:var(--white);font-family:"Montserrat",sans-serif;font-size:12px;font-weight:600;padding:14px 0}

/* footer */
.footer{position:absolute;left:0;top:2080px;width:1200px;height:532px;background:var(--dark)}
.footer .mark{position:absolute;left:0;right:0;top:60px;text-align:center;color:#9a9b9e;font-family:Georgia,serif;font-size:34px}
.footer h3{position:absolute;left:0;right:0;top:110px;text-align:center;color:var(--white);font-size:14px;font-weight:600}
.footer .intro{position:absolute;left:330px;top:142px;width:540px;text-align:center;color:#a4a6aa;font-size:11px;line-height:1.7}
.foot-logo{position:absolute;left:220px;top:290px;width:74px;height:50px;background:var(--red);display:flex;align-items:center;justify-content:center}
.foot-logo span{font-family:"Montserrat",sans-serif;font-weight:700;color:var(--white);font-size:18px}
.contact{position:absolute;left:320px;top:292px;color:#a4a6aa;font-size:10.5px;line-height:1.7}
.contact b{color:var(--white);font-weight:600}
.resources{position:absolute;left:720px;top:290px;width:260px;color:#a4a6aa;font-size:10.5px;line-height:1.7}
.resources b{color:var(--white);font-weight:600;display:block;margin-bottom:4px}
.resources li{list-style:none;padding-left:12px;position:relative}
.resources li::before{content:"";position:absolute;left:0;top:7px;width:5px;height:5px;background:var(--red)}
.foot-nav{position:absolute;left:220px;top:430px;width:760px;padding-top:18px;border-top:1px solid rgba(255,255,255,.12);display:flex;justify-content:center;gap:28px}
.foot-nav a{color:#c3c5c8;font-size:10px;text-decoration:none;font-family:"Montserrat",sans-serif;letter-spacing:.5px}
.copy{position:absolute;left:0;right:0;top:484px;text-align:center;color:#85878b;font-size:10px}
</style>
</head>
<body>

<header class="hero">
  <div class="hero-photo" role="img" aria-label="Downtown Dallas office towers against a blue sky"></div>
  <div class="hero-shade"></div>
  <div class="topbar">
    <div class="logo"><span>TBNW</span></div>
    <nav class="nav">
      <a href="#">HOME</a><a href="#">SERVICES</a><a href="#">ABOUT TBNW</a><a href="#">CONTACT US</a><a href="#">BLOG</a><a href="#">CLIENT LOGIN</a>
    </nav>
  </div>
  <h1>Professional Office And Warehouse Leasing</h1>
  <p class="lede">Find space your team will love, faster than you think, with representation that costs you nothing in the DFW area.</p>
  <a class="btn cta" href="#">Contact TBNW Today</a>
  <div class="phone">
    <svg width="18" height="18" viewBox="0 0 24 24"><path fill="#fff" d="M6.6 10.8a15.1 15.1 0 0 0 6.6 6.6l2.2-2.2c.3-.3.7-.4 1-.2 1.1.4 2.3.6 3.6.6.6 0 1 .4 1 1V20c0 .6-.4 1-1 1A17 17 0 0 1 3 4c0-.6.4-1 1-1h3.5c.6 0 1 .4 1 1 0 1.3.2 2.5.6 3.6.1.3 0 .7-.2 1z"/></svg>
    214-555-0148
  </div>
  <form class="lead-form">
    <h3>Looking for commercial real estate in the DFW area?</h3>
    <div class="field">Name *</div>
    <div class="field">Email *</div>
    <div class="field">Phone *</div>
    <div class="field tall">Message</div>
    <a class="btn" href="#">Get FREE Location Now</a>
  </form>
</header>

<section class="why">
  <h2 class="section-title">Why Tenant Representation?</h2>
  <div class="features">
    <div class="feature">
      <div class="icon"><svg width="22" height="22" viewBox="0 0 24 24" fill="none" stroke="#fff" stroke-width="2"><circle cx="8" cy="8" r="3"/><circle cx="16" cy="8" r="3"/><path d="M3 19c0-3 2-5 5-5s5 2 5 5M11 19c0-3 2-5 5-5s5 2 5 5"/></svg></div>
      <div><h3>Relationships</h3><p>We know the owners, brokers and landlords across the region, so doors open for you quickly and terms stay fair from the first tour to signing day.</p></div>
    </div>
    <div class="feature">
      <div class="icon"><svg width="22" height="22" viewBox="0 0 24 24" fill="none" stroke="#fff" stroke-width="2"><rect x="4" y="4" width="16" height="16"/><path d="M4 10h16M10 10v10"/></svg></div>
      <div><h3>Access to More</h3><p>See listings that never reach public sites, plus market data that shows what similar tenants truly pay for comparable space nearby.</p></div>
    </div>
    <div class="feature">
      <div class="icon"><svg width="22" height="22" viewBox="0 0 24 24" fill="none" stroke="#fff" stroke-width="2"><circle cx="12" cy="12" r="8"/><path d="M12 7v10M9 9.5c0-1 1.3-1.5 3-1.5s3 .7 3 1.8-1.5 1.5-3 2-3 1-3 2.2 1.3 1.8 3 1.8 3-.5 3-1.5"/></svg></div>
      <div><h3>Free To You</h3><p>Our fee is paid by the landlord, so your business gains expert guidance at no added cost while we work only for your interests.</p></div>
    </div>
    <div class="feature">
      <div class="icon"><svg width="22" height="22" viewBox="0 0 24 24" fill="none" stroke="#fff" stroke-width="2"><path d="M4 20h16M7 16V9M12 16V5M17 16v-4"/></svg></div>
      <div><h3>Customized Service</h3><p>Every search is shaped around your size, budget and timeline, with a clear plan and steady updates until you move in.</p></div>
    </div>
  </div>
</section>

<article class="founder">
  <div class="founder-photo" role="img" aria-label="Portrait of the firm's founder in a dark suit"></div>
  <p class="founder-text">For over two decades we have helped growing companies across Dallas secure office and warehouse space on better terms. We listen first, search wide and negotiate hard, so you can stay focused on running your business while we handle every detail of the lease from start to finish.</p>
  <p class="founder-name">Grant H. Morrow <span>– Founder and Partner</span></p>
  <a class="founder-next" href="#" aria-label="Next"><svg width="14" height="14" viewBox="0 0 24 24" fill="none" stroke="#fff" stroke-width="3"><path d="M8 4l8 8-8 8"/></svg></a>
</article>

<section class="testimonials">
  <div class="testimonials-photo" role="img" aria-label="Soft, faded view of a modern open office interior"></div>
  <h2 class="section-title">Client Testimonial</h2>
  <p class="ghost" style="left:130px">They found us a space that fit our crew and our budget, and the move was easy from start to end.</p>
  <p class="ghost" style="left:830px;text-align:right">Clear advice, quick answers and a lease we feel good about. We would call them again.</p>
  <blockquote class="quote-card">
    The team listened to what we needed and found three great options within a week. They handled every talk with the landlord and saved us real money on our new lease. Highly recommended.
    <span class="who">Celia Marchetti</span>
  </blockquote>
  <div class="avatar" style="left:215px;top:290px" role="img" aria-label="Client portrait"></div>
  <div class="avatar" style="left:583px;top:372px" role="img" aria-label="Client portrait"></div>
  <div class="avatar" style="left:950px;top:290px" role="img" aria-label="Client portrait"></div>
</section>

<section class="band">
  <p>Whether your lease is expiring soon, or you're just starting your search, TBNW can help you find the perfect space.</p>
  <a class="btn-outline" href="#">Make An Appointment</a>
</section>

<footer class="footer">
  <div class="mark">“</div>
  <h3>5 Important Key Aspects of Tenant Representation To Know</h3>
  <p class="intro">Before you sign a new lease, learn how a tenant advocate protects your budget, your timeline and your options in a busy market. Our short guide covers the steps most owners miss.</p>
  <div class="foot-logo"><span>TBNW</span></div>
  <div class="contact">
    <b>Contact Us</b><br>
    1420 Elm Street, Suite 300, Dallas, TX 75201<br>
    Ph: 214-555-0148 &nbsp; Fax: 214-555-0149
  </div>
  <div class="resources">
    <b>Free Tenant Guides</b>
    <ul>
      <li>How to compare lease offers side by side</li>
      <li>Planning a smooth office move in Dallas</li>
    </ul>
  </div>
  <nav class="foot-nav">
    <a href="#">HOME</a><a href="#">SERVICES</a><a href="#">OFFICE LEASING</a><a href="#">ABOUT US</a><a href="#">CONTACT</a><a href="#">BLOG</a><a href="#">PRIVACY</a><a href="#">SITE MAP</a>
  </nav>
  <p class="copy">Copyright © 2017 TBNW</p>
</footer>

</body>
</html>
```